Front signage

Our work consists of Industrial Electrical Automation.
We are an established company with a logo we are happy with.
Though we still need:
- a sign for our front door - 420mm x 1200mm
- a sign at the front of the building - 250mm x 1600mm

Please see attached our logo, and following our colour theme would be nice, but not essential.
Please see our website for more information on what we do
www.voltarispan.com.au

```html
<!DOCTYPE html>
<html lang="en">
<head>
<meta charset="utf-8">
<title>Voltarispan Services – Front Signage</title>
<link rel="stylesheet" href="https://fonts.googleapis.com/css2?family=Archivo:wdth,wght@62..125,800&family=Barlow+Semi+Condensed:wght@600&display=swap">
<style>
  :root {
    --brand-blue: #034a98;
    --brand-orange: #fc5000;
    --brand-grey: #56565b;
    --sign-white: #ffffff;
  }
  html, body {
    margin: 0;
    padding: 0;
    overflow: hidden;
    background: var(--sign-white);
  }
  .sign {
    position: relative;
    width: 1200px;
    height: 187px;
    background: var(--sign-white);
    overflow: hidden;
  }
  .sign__mark {
    position: absolute;
    left: 104px;
    top: 32px;
    width: 108px;
    height: 108px;
    background: var(--brand-blue);
  }
  .sign__lockup {
    position: absolute;
    left: 0;
    top: 0;
  }
  .sign__name {
    font-family: "Archivo", "Arial Black", sans-serif;
    font-weight: 800;
    font-stretch: 112%;
    font-size: 48px;
    fill: var(--brand-grey);
  }
  .sign__tagline {
    font-family: "Barlow Semi Condensed", "Arial Narrow", sans-serif;
    font-weight: 600;
    font-size: 27px;
    letter-spacing: 1px;
    fill: var(--brand-orange);
  }
  .sign__rule {
    stroke: var(--brand-orange);
    stroke-width: 1.2;
  }
  .sign__band {
    position: absolute;
    top: 171px;
    height: 16px;
  }
  .sign__band--blue {
    left: 0;
    width: 600px;
    background: var(--brand-blue);
  }
  .sign__band--orange {
    left: 600px;
    width: 600px;
    background: var(--brand-orange);
  }
</style>
</head>
<body>
  <main class="sign">
    <div class="sign__mark" aria-hidden="true"></div>

    <svg class="sign__lockup" width="1200" height="171" viewBox="0 0 1200 171">
      <text class="sign__name" x="320" y="93" textLength="830" lengthAdjust="spacingAndGlyphs">VOLTARISPAN SERVICES</text>

      <line class="sign__rule" x1="321" y1="121" x2="366" y2="121"/>
      <text class="sign__tagline" x="368" y="130" textLength="734" lengthAdjust="spacingAndGlyphs">INDUSTRIAL ELECTRICAL AND MECHANICAL SERVICES</text>
      <line class="sign__rule" x1="1105" y1="121" x2="1150" y2="121"/>
    </svg>

    <div class="sign__band sign__band--blue"></div>
    <div class="sign__band sign__band--orange"></div>
  </main>
</body>
</html>
```